Larkfield civic consultancy needs a business card design

Business card should represent civil engineering infrastructure projects such as roads, bridges, tunnels, rail, rail, pipelines, structures and resource infrastructure

```html
<!DOCTYPE html>
<html lang="en">
<head>
<meta charset="utf-8">
<title>Larkfield civic consultancy – business card</title>
<link rel="stylesheet" href="https://fonts.googleapis.com/css2?family=Rajdhani:ital,wght@0,500;0,600;0,700;1,500&display=swap">
<style>
  :root {
    --navy: #1f2c5c;
    --stone: #c9c7b8;
    --steel: #a39b91;
    --steel-dark: #958c82;
    --ink: #111111;
    --white: #ffffff;
    --page: #ffffff;
  }
  * { box-sizing: border-box; margin: 0; padding: 0; }
  html, body {
    width: 1200px; height: 1200px; overflow: hidden;
    background: var(--page);
    font-family: "Rajdhani", sans-serif;
  }
  .card {
    position: absolute;
    width: 878px; height: 555px;
    background: var(--stone);
    overflow: hidden;
  }
  .card--front { left: 44px; top: 20px; }
  .card--back { left: 284px; top: 611px; }

  .header-band {
    position: absolute; left: 0; top: 28px;
    width: 100%; height: 109px;
    background: var(--navy);
  }
  .brand {
    position: absolute;
    display: flex; align-items: center; gap: 14px;
    color: var(--white);
  }
  .brand-mark { width: 18px; height: 18px; background: var(--white); flex: none; }
  .brand-name {
    font-size: 40px; font-weight: 600; line-height: 1;
    letter-spacing: 6px; text-transform: uppercase;
  }
  .header-band .brand { left: 72px; top: 34px; }

  .holder {
    position: absolute; right: 61px; top: 30px; text-align: right;
    color: var(--white);
  }
  .holder-name { font-size: 35px; font-weight: 700; line-height: 1; }
  .holder-role { font-size: 21px; font-weight: 500; font-style: italic; margin-top: 6px; }

  .infrastructure-scene {
    position: absolute; left: 0; top: 268px; width: 100%; height: 242px;
    background: linear-gradient(180deg, var(--stone) 0%, var(--steel) 45%, var(--steel-dark) 100%);
    z-index: 1;
  }
  .contact-list {
    position: absolute; left: 70px; top: 174px; list-style: none;
    color: var(--ink); z-index: 2;
  }
  .contact-item { display: flex; align-items: center; height: 44px; }
  .contact-item:first-child { height: 44px; margin-bottom: 4px; }
  .contact-icon { width: 32px; height: 28px; margin-right: 24px; flex: none; }
  .contact-text { font-size: 22px; font-weight: 500; white-space: nowrap; }
  .contact-item:first-child .contact-text { font-size: 30px; }

  .footer-band {
    position: absolute; left: 0; bottom: 0; width: 100%; height: 45px;
    background: var(--navy); z-index: 2;
  }
  .tagline {
    position: absolute; right: 61px; top: 4px;
    color: var(--white); font-size: 27px; font-weight: 500; font-style: italic;
    letter-spacing: 1.5px;
  }
  .card--back .brand {
    left: 0; right: 0; top: 248px; justify-content: center;
  }
</style>
</head>
<body>
  <section class="card card--front" aria-label="Business card front">
    <header class="header-band">
      <div class="brand">
        <span class="brand-mark" aria-hidden="true"></span>
        <span class="brand-name">Larkfield</span>
      </div>
      <div class="holder">
        <div class="holder-name">Callum Rhys Avery</div>
        <div class="holder-role">Project Director</div>
      </div>
    </header>

    <div class="infrastructure-scene" role="img" aria-label="Mirrored silhouette of elevated road bridges, towers and industrial structures"></div>

    <ul class="contact-list">
      <li class="contact-item">
        <svg class="contact-icon" viewBox="0 0 32 28" aria-hidden="true">
          <rect x="10" y="2" width="13" height="24" rx="2" fill="var(--ink)"/>
          <rect x="12" y="6" width="9" height="7" fill="var(--stone)"/>
          <g fill="var(--stone)">
            <rect x="12" y="15" width="2" height="2"/><rect x="15.5" y="15" width="2" height="2"/><rect x="19" y="15" width="2" height="2"/>
            <rect x="12" y="19" width="2" height="2"/><rect x="15.5" y="19" width="2" height="2"/><rect x="19" y="19" width="2" height="2"/>
          </g>
        </svg>
        <span class="contact-text">+61400527193</span>
      </li>
      <li class="contact-item">
        <svg class="contact-icon" viewBox="0 0 32 28" aria-hidden="true">
          <rect x="1" y="6" width="30" height="17" fill="var(--ink)"/>
          <path d="M2 7 L16 17 L30 7 M2 22 L12 14 M30 22 L20 14" stroke="var(--stone)" stroke-width="1.6" fill="none"/>
        </svg>
        <span class="contact-text">callum.rhys.avery@mailhub.com</span>
      </li>
      <li class="contact-item">
        <svg class="contact-icon" viewBox="0 0 32 28" aria-hidden="true">
          <circle cx="16" cy="14" r="13" fill="var(--ink)"/>
          <ellipse cx="16" cy="14" rx="5.5" ry="12" fill="none" stroke="var(--stone)" stroke-width="1.4"/>
          <path d="M4 10 H28 M4 18 H28" stroke="var(--stone)" stroke-width="1.4"/>
        </svg>
        <span class="contact-text">callum.avery@larkfieldcivicconsultancy.com.au</span>
      </li>
    </ul>

    <footer class="footer-band">
      <span class="tagline">extreme engineering</span>
    </footer>
  </section>

  <section class="card card--back" aria-label="Business card back">
    <div class="brand">
      <span class="brand-mark" aria-hidden="true"></span>
      <span class="brand-name">Larkfield</span>
    </div>
  </section>
</body>
</html>
```